Spice Mix Label Bottle Branding - Health and Weight Loss Mixes

The company is called ZestRow Spice Mix's. We've created 5 spice mixes using ingredients that promote health and weight loss. We already have a logo but now we need labels for our bottles. We would like to see designs that have the feel of health supplements (see attached examples)

We would like a different colour featured with each of our flavours.

Our flavours are:
-Golden Chai (Yellow)
-Mild Curry (Orange)
-Coffee Rub (brown)
-Garlic Oregano (Green)
-Taco (Blue)

Thank you!

Target Market(s)

Ages 22-35. Men and Female. Trendy, Hipster.

Industry/Entity Type

Food Production

Font styles to use
Sans Serif

Colors
f37122
0655a3
0692cd
9bcb3c
fbee3f

Requirements
Must have
• A different featured colour for each flavour.
• The ZestRow Spices Logo (attached)
• The slogan: "Weight Loss Ingredients"
• -Golden Chai (Yellow)
• -Mild Curry (Orange)
• -Coffee Rub (brown)
• -Garlic Oregano (Green)
• -Taco (Blue)
• Text Files attached.
Nice to have
• A black label with a featured colour for each of the spice mice flavours.
• 'No Salt added'

```html
<!DOCTYPE html>
<html lang="en">
<head>
<meta charset="utf-8">
<title>ZestRow Spices – Bottle Labels</title>
<link href="https://fonts.googleapis.com/css2?family=Bebas+Neue&family=Oswald:wght@500;600&display=swap" rel="stylesheet">
<style>
  :root {
    --page: #ffffff;
    --label-black: #1d1d1d;
    --logo-white: #ffffff;
    --ink: #111111;
    --coffee: #a8703f;
    --chai: #d9a334;
    --curry: #f05a1a;
    --garlic: #9bbf3a;
    --taco: #3a6ea8;
  }
  * { box-sizing: border-box; margin: 0; padding: 0; }
  html, body { width: 1200px; height: 849px; overflow: hidden; background: var(--page); }
  .label-row {
    position: absolute; left: 0; top: 0; width: 1200px; height: 849px;
    display: flex; justify-content: center; align-items: center; gap: 30px;
  }
  .label {
    position: relative; width: 200px; height: 300px;
    background: var(--label-black); color: #fff;
  }
  .label--coffee { --accent: var(--coffee); }
  .label--chai { --accent: var(--chai); }
  .label--curry { --accent: var(--curry); }
  .label--garlic { --accent: var(--garlic); }
  .label--taco { --accent: var(--taco); }

  .brand-box {
    position: absolute; top: 0; left: 50%; transform: translateX(-50%);
    width: 96px; height: 60px; background: var(--logo-white);
    display: flex; flex-direction: column; align-items: center; justify-content: center;
    font-family: "Bebas Neue", sans-serif; color: var(--ink); line-height: 0.9;
  }
  .brand-box .brand-name { font-size: 26px; letter-spacing: 0.5px; }
  .brand-box .brand-sub { font-size: 11px; letter-spacing: 3px; }

  .ribbon { position: absolute; top: 50px; left: 12px; width: 176px; height: 30px; }
  .ribbon svg { position: absolute; inset: 0; width: 100%; height: 100%; }
  .ribbon .slogan {
    position: relative; display: block; text-align: center; line-height: 30px;
    font-family: "Oswald", sans-serif; font-weight: 600; font-size: 10.5px;
    letter-spacing: 0.3px; text-transform: uppercase; color: #fff;
  }

  .flavor {
    position: absolute; top: 96px; left: 0; right: 0; height: 110px;
    display: flex; align-items: center; justify-content: center; text-align: center;
    font-family: "Bebas Neue", sans-serif; font-size: 50px; line-height: 0.9;
    letter-spacing: 1px; color: #fff;
    text-shadow: 2px 2px 0 var(--accent), 3px 3px 0 var(--accent);
  }

  .no-salt {
    position: absolute; top: 222px; left: 16px; right: 16px;
    display: flex; align-items: center; gap: 8px;
    font-family: "Oswald", sans-serif; font-weight: 500; font-size: 10px;
    text-transform: uppercase; color: var(--accent); white-space: nowrap;
  }
  .no-salt::before, .no-salt::after {
    content: ""; flex: 1; height: 1px; background: var(--accent);
  }

  .net-size {
    position: absolute; top: 258px; left: 0; right: 0; text-align: center;
    font-family: "Oswald", sans-serif; font-weight: 500; font-size: 8px;
    text-transform: uppercase; color: #fff; letter-spacing: 0.3px;
  }
</style>
</head>
<body>
<main class="label-row">

  <article class="label label--coffee">
    <div class="brand-box"><span class="brand-name">ZestRow</span><span class="brand-sub">Spices</span></div>
    <div class="ribbon">
      <svg viewBox="0 0 176 30" preserveAspectRatio="none" aria-hidden="true">
        <polygon points="0,6 20,6 20,30 0,30 8,18" fill="var(--accent)"/>
        <polygon points="176,6 156,6 156,30 176,30 168,18" fill="var(--accent)"/>
        <polygon points="0,6 20,6 20,30 0,30 8,18" fill="#000" opacity="0.3"/>
        <polygon points="176,6 156,6 156,30 176,30 168,18" fill="#000" opacity="0.3"/>
        <rect x="14" y="0" width="148" height="25" fill="var(--accent)"/>
      </svg>
      <span class="slogan">Weight Loss Ingredients</span>
    </div>
    <h2 class="flavor">Coffee<br>Rub</h2>
    <p class="no-salt">No Salt Added</p>
    <p class="net-size">Net size 2oz</p>
  </article>

  <article class="label label--chai">
    <div class="brand-box"><span class="brand-name">ZestRow</span><span class="brand-sub">Spices</span></div>
    <div class="ribbon">
      <svg viewBox="0 0 176 30" preserveAspectRatio="none" aria-hidden="true">
        <polygon points="0,6 20,6 20,30 0,30 8,18" fill="var(--accent)"/>
        <polygon points="176,6 156,6 156,30 176,30 168,18" fill="var(--accent)"/>
        <polygon points="0,6 20,6 20,30 0,30 8,18" fill="#000" opacity="0.3"/>
        <polygon points="176,6 156,6 156,30 176,30 168,18" fill="#000" opacity="0.3"/>
        <rect x="14" y="0" width="148" height="25" fill="var(--accent)"/>
      </svg>
      <span class="slogan">Weight Loss Ingredients</span>
    </div>
    <h2 class="flavor">Golden<br>Chai</h2>
    <p class="no-salt">No Salt Added</p>
    <p class="net-size">Net size 2oz</p>
  </article>

  <article class="label label--curry">
    <div class="brand-box"><span class="brand-name">ZestRow</span><span class="brand-sub">Spices</span></div>
    <div class="ribbon">
      <svg viewBox="0 0 176 30" preserveAspectRatio="none" aria-hidden="true">
        <polygon points="0,6 20,6 20,30 0,30 8,18" fill="var(--accent)"/>
        <polygon points="176,6 156,6 156,30 176,30 168,18" fill="var(--accent)"/>
        <polygon points="0,6 20,6 20,30 0,30 8,18" fill="#000" opacity="0.3"/>
        <polygon points="176,6 156,6 156,30 176,30 168,18" fill="#000" opacity="0.3"/>
        <rect x="14" y="0" width="148" height="25" fill="var(--accent)"/>
      </svg>
      <span class="slogan">Weight Loss Ingredients</span>
    </div>
    <h2 class="flavor">Mild<br>Curry</h2>
    <p class="no-salt">No Salt Added</p>
    <p class="net-size">Net size 2oz</p>
  </article>

  <article class="label label--garlic">
    <div class="brand-box"><span class="brand-name">ZestRow</span><span class="brand-sub">Spices</span></div>
    <div class="ribbon">
      <svg viewBox="0 0 176 30" preserveAspectRatio="none" aria-hidden="true">
        <polygon points="0,6 20,6 20,30 0,30 8,18" fill="var(--accent)"/>
        <polygon points="176,6 156,6 156,30 176,30 168,18" fill="var(--accent)"/>
        <polygon points="0,6 20,6 20,30 0,30 8,18" fill="#000" opacity="0.3"/>
        <polygon points="176,6 156,6 156,30 176,30 168,18" fill="#000" opacity="0.3"/>
        <rect x="14" y="0" width="148" height="25" fill="var(--accent)"/>
      </svg>
      <span class="slogan">Weight Loss Ingredients</span>
    </div>
    <h2 class="flavor">Garlic<br>Oregano</h2>
    <p class="no-salt">No Salt Added</p>
    <p class="net-size">Net size 2oz</p>
  </article>

  <article class="label label--taco">
    <div class="brand-box"><span class="brand-name">ZestRow</span><span class="brand-sub">Spices</span></div>
    <div class="ribbon">
      <svg viewBox="0 0 176 30" preserveAspectRatio="none" aria-hidden="true">
        <polygon points="0,6 20,6 20,30 0,30 8,18" fill="var(--accent)"/>
        <polygon points="176,6 156,6 156,30 176,30 168,18" fill="var(--accent)"/>
        <polygon points="0,6 20,6 20,30 0,30 8,18" fill="#000" opacity="0.3"/>
        <polygon points="176,6 156,6 156,30 176,30 168,18" fill="#000" opacity="0.3"/>
        <rect x="14" y="0" width="148" height="25" fill="var(--accent)"/>
      </svg>
      <span class="slogan">Weight Loss Ingredients</span>
    </div>
    <h2 class="flavor">Taco</h2>
    <p class="no-salt">No Salt Added</p>
    <p class="net-size">Net size 2oz</p>
  </article>

</main>
</body>
</html>
```